Lantern Hill Publicity is a new boutique Press Office with a small roster of well-chosen clients across an array of disciplines; from Art and Technology to Restaurants and Fashion. Based in Greenpoint Brooklyn, Lantern Hill Publicity achieves outstanding results through hard work, tenacity, efficiency and a sense of humor. We need a simple, versatile and classic design. We would like each side of the card to be white text on a black background.

Boutique

```html
<!DOCTYPE html>
<html lang="en">
<head>
<meta charset="utf-8">
<title>Lantern Hill Publicity — Business Card</title>
<link href="https://fonts.googleapis.com/css2?family=Playfair+Display:wght@500;600&family=Lato:wght@400&display=swap" rel="stylesheet">
<style>
  :root {
    --backdrop: #2b2b2d;
    --card: #1f2023;
    --ink: #ffffff;
    --ink-soft: #e9e9e9;
    --rule: #d8d8d8;
    --icon-glyph: #1f2023;
  }
  * { box-sizing: border-box; margin: 0; padding: 0; }
  html, body {
    width: 1189px; height: 1200px; overflow: hidden;
    background: var(--backdrop);
  }
  .canvas { position: relative; width: 1189px; height: 1200px; }
  .card {
    position: absolute; left: 173px; width: 854px; height: 487px;
    background: var(--card); border-radius: 18px; color: var(--ink);
  }
  .card--front { top: 68px; }
  .card--back { top: 627px; }

  .brand-name {
    font-family: "Playfair Display", serif; font-weight: 500;
    color: var(--ink); text-transform: uppercase; text-align: center;
    line-height: 1.35;
  }
  .card--front .brand-name {
    position: absolute; left: 0; right: 0; top: 170px;
    font-size: 44px; letter-spacing: 6px;
  }
  .card--back .brand-name {
    position: absolute; left: 17px; width: 400px; top: 185px;
    font-size: 30px; letter-spacing: 4px;
  }

  .divider {
    position: absolute; left: 417px; top: 95px; width: 1px; height: 297px;
    background: var(--rule);
  }
  .person {
    position: absolute; left: 454px; top: 96px;
  }
  .person__name {
    font-family: "Playfair Display", serif; font-weight: 600;
    font-size: 31px; text-transform: uppercase; line-height: 1;
  }
  .person__title {
    font-family: "Lato", sans-serif; font-size: 22px; color: var(--ink-soft);
    margin-top: 6px;
  }
  .contact {
    position: absolute; left: 454px; top: 230px;
    font-family: "Lato", sans-serif; font-size: 22.5px; color: var(--ink-soft);
  }
  .contact__address { line-height: 30px; margin-bottom: 12px; }
  .contact__row { display: flex; align-items: center; height: 30.5px; }
  .contact__icon { width: 22px; height: 22px; margin-right: 16px; flex: none; }
</style>
</head>
<body>
<main class="canvas">

  <section class="card card--front" aria-label="Card front">
    <p class="brand-name">Lantern Hill<br>Publicity</p>
  </section>

  <section class="card card--back" aria-label="Card back">
    <p class="brand-name">Lantern Hill<br>Publicity</p>
    <div class="divider"></div>

    <div class="person">
      <p class="person__name">Clara Whitfield</p>
      <p class="person__title">Chief Executive Officer</p>
    </div>

    <div class="contact">
      <p class="contact__address">Your Address,2nd Ste<br>Ashford, Maine 1234</p>

      <p class="contact__row">
        <svg class="contact__icon" viewBox="0 0 22 22" aria-hidden="true">
          <rect width="22" height="22" rx="3" fill="var(--ink)"/>
          <path d="M7 5c1 0 2 2.5 2 3s-1 1-1 1.5c0 1 2.5 4 3.5 4 .5 0 1-1 1.5-1s3 1 3 2-1.5 2.5-2.5 2.5C9 17 5 12 5 7.5 5 6 6 5 7 5z" fill="var(--icon-glyph)"/>
        </svg>
        123 456 7890
      </p>
      <p class="contact__row">
        <svg class="contact__icon" viewBox="0 0 22 22" aria-hidden="true">
          <rect width="22" height="22" rx="3" fill="var(--ink)"/>
          <rect x="4" y="6" width="14" height="10" fill="none" stroke="var(--icon-glyph)" stroke-width="1.6"/>
          <path d="M4 6l7 6 7-6" fill="none" stroke="var(--icon-glyph)" stroke-width="1.6"/>
        </svg>
        your@yourcompany.com
      </p>
      <p class="contact__row">
        <svg class="contact__icon" viewBox="0 0 22 22" aria-hidden="true">
          <rect width="22" height="22" rx="3" fill="var(--ink)"/>
          <g fill="none" stroke="var(--icon-glyph)" stroke-width="1.4">
            <circle cx="11" cy="11" r="6.5"/>
            <ellipse cx="11" cy="11" rx="3" ry="6.5"/>
            <path d="M4.5 11h13M5.5 7.8h11M5.5 14.2h11"/>
          </g>
        </svg>
        www.yourcompany.com
      </p>
    </div>
  </section>

</main>
</body>
</html>
```